Business Card for Orvane Parts Wholesale supplier

Hi There! I need a new business card for our company. We are specialized in selling Orvane parts, mostly we sell new LCD screens for Telvox and Slatrons. I would like to see that back in the design.

You can find the colors and logo's on our website: www.dorvak-example.nl

Industry/Entity Type

Business

Contact Information for Business Card

My Details:
Lars Vintorp

Phone: 0031612873406
E-mail: Lars@dorvak-example.nl

Slogan: "Because Quality Matters"

Font styles to use
Sans Serif

Colors

Designer to choose colors to be used in the design.

Requirements
Must have
• A Black backside with the Dorvak logo on it. The front side should be clean with only my contact details.
• But I'm also open for something really different or awesome!
Nice to have
• Remember that we are in the parts & repairing industry, So i'll be handing those business cards mainly to repair companies. Maybe you can do something with that thought :)

```html
<!DOCTYPE html>
<html lang="en">
<head>
<meta charset="utf-8">
<title>Dorvak Business Card</title>
<link href="https://fonts.googleapis.com/css2?family=Open+Sans:wght@400;600;700;800&display=swap" rel="stylesheet">
<style>
  :root {
    --stage: #d9d6d2;
    --card-black: #141415;
    --card-front: #1f1f21;
    --orange: #f36f21;
    --grey-band: #a7a7aa;
    --white: #ffffff;
    --muted: #d0d0d2;
    --emboss: #2b2b2d;
    --faint: rgba(255,255,255,0.035);
  }
  * { margin: 0; padding: 0; box-sizing: border-box; }
  html, body {
    width: 1200px; height: 715px; overflow: hidden;
    background: var(--stage);
    font-family: "Open Sans", Arial, sans-serif;
  }
  .canvas {
    position: relative; width: 1200px; height: 715px;
    display: flex; align-items: center; justify-content: center; gap: 60px;
  }
  .card {
    position: relative; width: 520px; height: 297px; overflow: hidden;
    box-shadow: 0 10px 28px rgba(0,0,0,0.28);
  }
  /* Back side */
  .card-back { background: var(--card-black); display: flex; align-items: center; justify-content: center; gap: 14px; }
  .back-mark { width: 34px; height: 34px; background: var(--emboss); }
  .back-name { color: var(--emboss); font-weight: 800; font-size: 58px; letter-spacing: -1px; line-height: 1; }
  /* Front side */
  .card-front { background: var(--card-front); }
  .faint-circle {
    position: absolute; width: 230px; height: 230px; border-radius: 50%;
    left: 270px; top: 60px; border: 44px solid var(--faint);
  }
  .brand { position: absolute; left: 36px; top: 34px; display: flex; align-items: center; gap: 12px; }
  .brand-mark { width: 40px; height: 40px; background: var(--orange); }
  .brand-name { color: var(--white); font-weight: 800; font-size: 58px; line-height: 1; letter-spacing: -1px; }
  .holder { position: absolute; left: 36px; top: 150px; }
  .holder-name { color: var(--white); font-weight: 700; font-size: 17px; }
  .holder-role { color: var(--muted); font-size: 11px; margin-top: 1px; }
  .contact { position: absolute; left: 318px; top: 132px; list-style: none; }
  .contact li { display: flex; align-items: center; gap: 10px; color: var(--white); font-size: 12.5px; height: 20px; }
  .contact svg { width: 13px; height: 13px; fill: var(--orange); flex: none; }
  .bands { position: absolute; left: 0; top: 0; }
  .slogan {
    position: absolute; right: 0; top: 254px; width: 270px; text-align: center;
    color: var(--white); font-size: 14px;
  }
</style>
</head>
<body>
  <main class="canvas">
    <section class="card card-back" aria-label="Card back">
      <span class="back-mark"></span>
      <span class="back-name">dorvak</span>
    </section>

    <section class="card card-front" aria-label="Card front">
      <div class="faint-circle"></div>
      <svg class="bands" width="520" height="297" viewBox="0 0 520 297">
        <polygon points="0,232 268,232 257,246 0,246" fill="var(--grey-band)"/>
        <polygon points="282,218 520,218 520,297 220,297" fill="var(--orange)"/>
      </svg>

      <div class="brand">
        <span class="brand-mark"></span>
        <span class="brand-name">dorvak</span>
      </div>

      <div class="holder">
        <p class="holder-name">Lars Vintorp</p>
        <p class="holder-role">Managing Director</p>
      </div>

      <ul class="contact">
        <li>
          <svg viewBox="0 0 24 24"><path d="M6.6 10.8a15 15 0 0 0 6.6 6.6l2.2-2.2a1 1 0 0 1 1-.25 11.4 11.4 0 0 0 3.6.57 1 1 0 0 1 1 1V20a1 1 0 0 1-1 1A17 17 0 0 1 3 4a1 1 0 0 1 1-1h3.5a1 1 0 0 1 1 1c0 1.25.2 2.45.57 3.57a1 1 0 0 1-.25 1z"/></svg>
          0031612873406
        </li>
        <li>
          <svg viewBox="0 0 24 24"><path d="M2 5h20v14H2z M2 5l10 8 10-8" fill="var(--orange)"/><path d="M3 6l9 7 9-7" fill="none" stroke="var(--card-front)" stroke-width="1.6"/></svg>
          Lars@dorvak-example.nl
        </li>
        <li>
          <svg viewBox="0 0 24 24"><circle cx="12" cy="12" r="10"/><path d="M2 12h20M12 2c3 3 3 17 0 20M12 2c-3 3-3 17 0 20" fill="none" stroke="var(--card-front)" stroke-width="1.5"/></svg>
          www.dorvak-example.nl
        </li>
      </ul>

      <p class="slogan">Because Quality Matters</p>
    </section>
  </main>
</body>
</html>
```